Internal Web Pages for Metrivane Labs

I need internal web pages (Why Metrivane Labs?, What We Offer, Blog, Testimonials) that match the design of the homepage. These do not need to be as long or in-depth as the landing page (provided for reference) but I will need three, maybe four, total pages (I'll select the max number of pages for now, but these will all be simple and short pages). Also attached is our new logo design for the company.

They are to essentially be:
Why Metrivane Labs? - An About Us and Why Choose Us page rolled into one.
What We Offer - A Services type page
Blog - self-explanatory
Testimonials - Customer Reviews and Use Cases

Also, maybe a very simple "Contact Us" page as well.

Target Market(s)

Business professionals that work with data analytics teams

Industry/Entity Type

Data Science

Number of Pages Required

5+ page

Requirements
Must have
• It must match the original design in theme and colors.
Nice to have
• Simple pages that show continuity that flows from the original landing page.
Should not have
• Can not be a different design that does not match the landing page.

```html
<!DOCTYPE html>
<html lang="en">
<head>
<meta charset="utf-8">
<title>Metrivane Labs – Blog Pages</title>
<link href="https://fonts.googleapis.com/css2?family=Poppins:wght@300;400;600;700&family=Roboto:ital,wght@0,400;0,500;0,700;1,400;1,500&family=Roboto+Slab:wght@300;400&display=swap" rel="stylesheet">
<style>
:root{
  --backdrop:#5d6be8;
  --brand:#5b5fd6;
  --ink:#1d1b3a;
  --body:#4a4a5a;
  --muted:#6b6b7b;
  --orange:#f07c00;
  --footer:#1a0845;
  --footer-deep:#140537;
  --line:#e3e3ec;
  --white:#fff;
}
*{box-sizing:border-box;margin:0;padding:0}
html,body{width:1079px;height:1200px;overflow:hidden}
body{background:var(--backdrop);font-family:'Roboto',sans-serif;color:var(--ink)}
.stage{position:absolute;left:0;top:0;width:1820px;height:2024px;transform:scale(.59286);transform-origin:0 0}
.page{position:absolute;top:127px;width:779px;background:var(--white);overflow:hidden}
.page--list{left:103px;height:1741px}
.page--post{left:971px;height:1229px}

/* header */
.site-header{position:absolute;left:0;top:0;width:779px;height:56px;background:var(--white)}
.page--post .site-header{border-bottom:2px solid var(--brand);height:58px}
.brand{position:absolute;top:12px;display:flex;align-items:center;gap:8px;font-family:'Poppins',sans-serif;font-weight:300;font-size:23px;color:#2b2966;white-space:nowrap}
.brand__mark{width:14px;height:14px;background:var(--brand)}
.nav{position:absolute;top:19px;display:flex;gap:20px;font-family:'Poppins',sans-serif;font-size:12.5px;color:#3a3a4a}
.nav__item--active{color:var(--brand)}
.btn-start{position:absolute;top:14px;width:86px;height:26px;background:var(--orange);color:var(--white);font-family:'Poppins',sans-serif;font-weight:700;font-size:8.5px;letter-spacing:.4px;display:flex;align-items:center;justify-content:center;box-shadow:0 3px 6px rgba(240,124,0,.35)}

/* hero */
.hero{position:absolute;left:0;top:56px;width:779px;height:270px}
.hero svg{position:absolute;left:0;top:0}
.hero__title{position:absolute;left:78px;top:90px;font-family:'Poppins',sans-serif;font-weight:300;font-size:26px;color:var(--white)}

.section-title{position:absolute;left:0;width:779px;text-align:center;font-family:'Poppins',sans-serif;font-weight:400;font-size:26px;color:#262450}
.section-title::after{content:"";display:block;width:94px;height:1px;background:#3a3a7a;margin:8px auto 0}

.date-badge{position:absolute;border-radius:50%;background:var(--brand);color:var(--white);font-family:'Roboto',sans-serif;font-weight:700;font-size:8px;line-height:9px;text-align:center;display:flex;align-items:center;justify-content:center;box-shadow:0 0 0 3px rgba(255,255,255,.25)}

.media{position:absolute;border-radius:0}

.meta{display:flex;gap:14px;font-style:italic;font-weight:500;font-size:9px;color:#2a2a3a;align-items:center}
.meta span{display:flex;align-items:center;gap:5px}
.meta svg{flex:none}

.btn-more{display:inline-flex;align-items:center;gap:4px;height:24px;padding:0 14px;border:1.5px solid var(--brand);border-radius:14px;color:var(--brand);font-weight:700;font-size:7.5px;letter-spacing:.3px}

/* featured */
.feature-card{position:absolute;left:372px;top:470px;width:306px;height:225px;background:var(--white);border:1px solid var(--line);border-radius:6px;box-shadow:0 4px 14px rgba(30,30,80,.08);padding:28px 25px 0}
.feature-card__title{font-weight:700;font-size:10.5px;line-height:13px;text-transform:uppercase;color:var(--ink)}
.feature-card .meta{margin-top:9px}
.feature-card__text{margin-top:12px;font-family:'Roboto Slab',serif;font-weight:300;font-size:7.6px;line-height:14px;color:var(--body)}
.feature-card .btn-more{margin-top:8px}

/* grid cards */
.post-card{position:absolute;width:186px;height:290px}
.post-card__media{position:absolute;left:0;top:0;width:186px;height:160px}
.post-card__body{position:absolute;left:7px;right:7px;top:120px;height:170px;background:var(--white);border:1px solid var(--line);border-radius:4px;padding:18px 15px 0}
.post-card__title{font-weight:700;font-size:9.3px;line-height:13px;text-transform:uppercase;color:var(--ink)}
.post-card .meta{margin-top:8px;font-size:8.6px}
.post-card__text{margin-top:6px;font-size:9.4px;line-height:14px;color:var(--body)}
.post-card .btn-more{margin-top:12px}
.post-card .date-badge{left:147px;top:12px;width:30px;height:30px}

/* single post */
.article{position:absolute;left:107px;top:399px;width:566px;height:458px;background:var(--white);border:1px solid var(--line);border-radius:3px;box-shadow:0 3px 10px rgba(30,30,80,.06);padding:21px 24px 0}
.article__title{font-weight:700;font-size:11px;line-height:17px;text-transform:uppercase;color:var(--ink)}
.article .meta{margin-top:8px}
.article__text{margin-top:13px;font-family:'Roboto Slab',serif;font-weight:300;font-size:10px;line-height:18.2px;color:var(--body)}
.article__text + .article__text{margin-top:26px}

/* footer */
.site-footer{position:absolute;left:0;bottom:0;width:779px;height:314px;background:var(--footer);color:var(--white)}
.site-footer .brand{left:90px;top:43px;color:var(--white)}
.footer-about{position:absolute;left:93px;top:86px;width:190px;font-size:10.3px;line-height:14.6px;color:#d9d6ee}
.socials{position:absolute;left:94px;top:170px;display:flex;gap:5px}
.socials span{width:22px;height:22px;border:1px solid #cfcce6;border-radius:50%}
.footer-heading{position:absolute;top:43px;font-weight:700;font-size:12px;letter-spacing:.3px}
.contact-list{position:absolute;left:311px;top:74px;list-style:none;font-size:10px;line-height:14px;font-weight:500;letter-spacing:.3px}
.contact-list li{display:flex;gap:12px;margin-bottom:13px}
.contact-list svg{flex:none;margin-top:2px}
.signup{position:absolute;left:489px;top:72px;width:197px}
.signup p{font-size:8.7px;line-height:15px;color:#d9d6ee}
.signup__input{margin-top:12px;height:25px;background:var(--white);border:1px solid #ccc;color:#666;font-size:8.7px;padding:0 12px;display:flex;align-items:center}
.signup__btn{margin-top:12px;width:82px;height:25px;background:var(--orange);font-weight:700;font-size:8.5px;display:flex;align-items:center;justify-content:center}
.footer-bar{position:absolute;left:0;bottom:0;width:100%;height:59px;background:var(--footer-deep);display:flex;align-items:center;justify-content:center;font-size:9.6px;font-weight:500}
</style>
</head>
<body>
<div class="stage">

  <!-- Blog listing page -->
  <section class="page page--list">
    <header class="site-header">
      <div class="brand" style="left:75px"><span class="brand__mark"></span>Metrivane Labs</div>
      <nav class="nav" style="left:304px"><span class="nav__item--active">Home</span><span>About us</span><span>Our Service</span><span>Blog</span><span>Contact</span></nav>
      <div class="btn-start" style="left:635px">GET STARTED</div>
    </header>

    <div class="hero">
      <svg width="779" height="270" viewBox="0 0 779 270" role="img" aria-label="Photo of hands typing on a laptop with glowing data network overlay">
        <defs>
          <linearGradient id="heroGrad" x1="0" y1="0" x2="1" y2="1">
            <stop offset="0" stop-color="#3a2f4a"/>
            <stop offset=".45" stop-color="#2a3b6e"/>
            <stop offset="1" stop-color="#2b1f5e"/>
          </linearGradient>
        </defs>
        <polygon points="0,0 779,0 779,192 390,252 0,199" fill="url(#heroGrad)"/>
        <polygon points="0,199 390,252 779,192 779,196 392,264 0,203" fill="#5b5fd6"/>
      </svg>
      <div class="hero__title">Latest Blogs</div>
    </div>

    <h2 class="section-title" style="top:370px">Our Blog Posts</h2>

    <div class="media" role="img" aria-label="Photo of a businessman holding a tablet with analytics dashboards" style="left:92px;top:445px;width:327px;height:274px;border-radius:8px;background:linear-gradient(135deg,#1a2440,#2c3e66 55%,#111a30)"></div>
    <div class="date-badge" style="left:104px;top:462px;width:30px;height:30px">OCT<br>2021</div>
    <article class="feature-card">
      <h3 class="feature-card__title">Lorem Ipsum is simply dummy text of the printing and typesetting industry.</h3>
      <div class="meta">
        <span><svg width="9" height="8" viewBox="0 0 9 8"><path d="M1 1h7v4.5H4L2 7V5.5H1z" fill="none" stroke="#5b5fd6" stroke-width="1"/></svg>2 comments</span>
        <span><svg width="8" height="8" viewBox="0 0 8 8"><circle cx="4" cy="2.2" r="2" fill="#5b5fd6"/><path d="M0 8c0-2.5 2-3.5 4-3.5S8 5.5 8 8z" fill="#5b5fd6"/></svg>by Nora</span>
      </div>
      <p class="feature-card__text">Lorem Ipsum is simply dummy text of the printing and typesetting industry. Lorem Ipsum has been the industry's standard dummy text ever since the 1500s, when an unknown printer took a galley of type and scrambled it to make a type specimen book. It has survived not only five centuries, but also the leap into electronic typesetting, remaining essentially</p>
      <span class="btn-more">LERN MORE <svg width="7" height="7" viewBox="0 0 7 7"><path d="M0 3.5h5M3 1l2.5 2.5L3 6" stroke="#5b5fd6" stroke-width="1.4" fill="none"/></svg></span>
    </article>

    <!-- grid row 1 -->
    <div class="post-card" style="left:94px;top:772px">
      <div class="post-card__media" role="img" aria-label="Photo of two colleagues discussing charts on a wall display" style="background:linear-gradient(135deg,#6d7f9a,#c8d0dc 60%,#8d95a6)"></div>
      <div class="date-badge">OCT<br>2021</div>
      <div class="post-card__body">
        <h3 class="post-card__title">Nemo enim ipsam volupta quia voluptas sit</h3>
        <div class="meta"><span><svg width="9" height="8" viewBox="0 0 9 8"><path d="M1 1h7v4.5H4L2 7V5.5H1z" fill="none" stroke="#5b5fd6"/></svg>2 comments</span><span><svg width="8" height="8" viewBox="0 0 8 8"><circle cx="4" cy="2.2" r="2" fill="#5b5fd6"/><path d="M0 8c0-2.5 2-3.5 4-3.5S8 5.5 8 8z" fill="#5b5fd6"/></svg>by Nora</span></div>
        <p class="post-card__text">Sed ut perspiciatis unde omnis iste natus error sit voluptatem accustium dlorue laum</p>
        <span class="btn-more">LERN MORE <svg width="7" height="7" viewBox="0 0 7 7"><path d="M0 3.5h5M3 1l2.5 2.5L3 6" stroke="#5b5fd6" stroke-width="1.4" fill="none"/></svg></span>
      </div>
    </div>
    <div class="post-card" style="left:296px;top:772px">
      <div class="post-card__media" role="img" aria-label="Photo of an analyst at screens full of data" style="background:linear-gradient(135deg,#3a3326,#1f2a2a 55%,#2b3a3a)"></div>
      <div class="date-badge">OCT<br>2021</div>
      <div class="post-card__body">
        <h3 class="post-card__title">Nemo enim ipsam volupta quia voluptas sit</h3>
        <div class="meta"><span><svg width="9" height="8" viewBox="0 0 9 8"><path d="M1 1h7v4.5H4L2 7V5.5H1z" fill="none" stroke="#5b5fd6"/></svg>2 comments</span><span><svg width="8" height="8" viewBox="0 0 8 8"><circle cx="4" cy="2.2" r="2" fill="#5b5fd6"/><path d="M0 8c0-2.5 2-3.5 4-3.5S8 5.5 8 8z" fill="#5b5fd6"/></svg>by Nora</span></div>
        <p class="post-card__text">Sed ut perspiciatis unde omnis iste natus error sit voluptatem accustium dlorue laum</p>
        <span class="btn-more">LERN MORE <svg width="7" height="7" viewBox="0 0 7 7"><path d="M0 3.5h5M3 1l2.5 2.5L3 6" stroke="#5b5fd6" stroke-width="1.4" fill="none"/></svg></span>
      </div>
    </div>
    <div class="post-card" style="left:499px;top:772px">
      <div class="post-card__media" role="img" aria-label="Photo of a hand touching a glowing holographic chart" style="background:linear-gradient(135deg,#0e2744,#1d5a8a 55%,#0b1e36)"></div>
      <div class="date-badge">OCT<br>2021</div>
      <div class="post-card__body">
        <h3 class="post-card__title">Nemo enim ipsam volupta quia voluptas sit</h3>
        <div class="meta"><span><svg width="9" height="8" viewBox="0 0 9 8"><path d="M1 1h7v4.5H4L2 7V5.5H1z" fill="none" stroke="#5b5fd6"/></svg>2 comments</span><span><svg width="8" height="8" viewBox="0 0 8 8"><circle cx="4" cy="2.2" r="2" fill="#5b5fd6"/><path d="M0 8c0-2.5 2-3.5 4-3.5S8 5.5 8 8z" fill="#5b5fd6"/></svg>by Nora</span></div>
        <p class="post-card__text">Sed ut perspiciatis unde omnis iste natus error sit voluptatem accustium dlorue laum</p>
        <span class="btn-more">LERN MORE <svg width="7" height="7" viewBox="0 0 7 7"><path d="M0 3.5h5M3 1l2.5 2.5L3 6" stroke="#5b5fd6" stroke-width="1.4" fill="none"/></svg></span>
      </div>
    </div>

    <!-- grid row 2 -->
    <div class="post-card" style="left:92px;top:1093px">
      <div class="post-card__media" role="img" aria-label="Photo of a laptop showing a world data dashboard" style="background:linear-gradient(135deg,#c9cdd6,#2b4f86 50%,#1a2d56)"></div>
      <div class="date-badge">OCT<br>2021</div>
      <div class="post-card__body">
        <h3 class="post-card__title">Nemo enim ipsam volupta quia voluptas sit</h3>
        <div class="meta"><span><svg width="9" height="8" viewBox="0 0 9 8"><path d="M1 1h7v4.5H4L2 7V5.5H1z" fill="none" stroke="#5b5fd6"/></svg>2 comments</span><span><svg width="8" height="8" viewBox="0 0 8 8"><circle cx="4" cy="2.2" r="2" fill="#5b5fd6"/><path d="M0 8c0-2.5 2-3.5 4-3.5S8 5.5 8 8z" fill="#5b5fd6"/></svg>by Nora</span></div>
        <p class="post-card__text">Sed ut perspiciatis unde omnis iste natus error sit voluptatem accustium dlorue laum</p>
        <span class="btn-more">LERN MORE <svg width="7" height="7" viewBox="0 0 7 7"><path d="M0 3.5h5M3 1l2.5 2.5L3 6" stroke="#5b5fd6" stroke-width="1.4" fill="none"/></svg></span>
      </div>
    </div>
    <div class="post-card" style="left:294px;top:1093px">
      <div class="post-card__media" role="img" aria-label="Photo of a laptop on a desk with charts on screen" style="background:linear-gradient(135deg,#3d3a36,#5f86a8 55%,#2d2a27)"></div>
      <div class="date-badge">OCT<br>2021</div>
      <div class="post-card__body">
        <h3 class="post-card__title">Nemo enim ipsam volupta quia voluptas sit</h3>
        <div class="meta"><span><svg width="9" height="8" viewBox="0 0 9 8"><path d="M1 1h7v4.5H4L2 7V5.5H1z" fill="none" stroke="#5b5fd6"/></svg>2 comments</span><span><svg width="8" height="8" viewBox="0 0 8 8"><circle cx="4" cy="2.2" r="2" fill="#5b5fd6"/><path d="M0 8c0-2.5 2-3.5 4-3.5S8 5.5 8 8z" fill="#5b5fd6"/></svg>by Nora</span></div>
        <p class="post-card__text">Sed ut perspiciatis unde omnis iste natus error sit voluptatem accustium dlorue laum</p>
        <span class="btn-more">LERN MORE <svg width="7" height="7" viewBox="0 0 7 7"><path d="M0 3.5h5M3 1l2.5 2.5L3 6" stroke="#5b5fd6" stroke-width="1.4" fill="none"/></svg></span>
      </div>
    </div>
    <div class="post-card" style="left:497px;top:1093px">
      <div class="post-card__media" role="img" aria-label="Photo of hands with hexagon data interface overlay" style="background:linear-gradient(135deg,#1d2226,#39444a 55%,#15191c)"></div>
      <div class="date-badge">OCT<br>2021</div>
      <div class="post-card__body">
        <h3 class="post-card__title">Nemo enim ipsam volupta quia voluptas sit</h3>
        <div class="meta"><span><svg width="9" height="8" viewBox="0 0 9 8"><path d="M1 1h7v4.5H4L2 7V5.5H1z" fill="none" stroke="#5b5fd6"/></svg>2 comments</span><span><svg width="8" height="8" viewBox="0 0 8 8"><circle cx="4" cy="2.2" r="2" fill="#5b5fd6"/><path d="M0 8c0-2.5 2-3.5 4-3.5S8 5.5 8 8z" fill="#5b5fd6"/></svg>by Nora</span></div>
        <p class="post-card__text">Sed ut perspiciatis unde omnis iste natus error sit voluptatem accustium dlorue laum</p>
        <span class="btn-more">LERN MORE <svg width="7" height="7" viewBox="0 0 7 7"><path d="M0 3.5h5M3 1l2.5 2.5L3 6" stroke="#5b5fd6" stroke-width="1.4" fill="none"/></svg></span>
      </div>
    </div>

    <footer class="site-footer">
      <div class="brand"><span class="brand__mark"></span>Metrivane Labs</div>
      <p class="footer-about">Sed ut perspiciatis unde omnis iste natus error sit voluptatem accusantium dolorque laudantium, totam rem aperiam, eaque ipsa quae ab illo inventore veritatis et quasi</p>
      <div class="socials"><span></span><span></span><span></span><span></span></div>
      <h4 class="footer-heading" style="left:311px">CONTACT US</h4>
      <ul class="contact-list">
        <li><svg width="10" height="13" viewBox="0 0 10 13"><path d="M5 12S1 7.5 1 4.8a4 4 0 0 1 8 0C9 7.5 5 12 5 12z" fill="none" stroke="#fff"/><circle cx="5" cy="4.8" r="1.4" fill="none" stroke="#fff"/></svg><span>Metrivane Labs<br>250 ipsam voluptatem<br>quia voluptas</span></li>
        <li><svg width="11" height="11" viewBox="0 0 11 11"><path d="M2 1l2 2.5-1.2 1.2a6 6 0 0 0 3.5 3.5L7.5 7 10 9l-1.3 1.5C4.5 10.5.5 6.5.5 2.3z" fill="none" stroke="#fff"/></svg><span>Phone :<br>555-0142-3100</span></li>
        <li><svg width="12" height="9" viewBox="0 0 12 9"><rect x=".5" y=".5" width="11" height="8" fill="none" stroke="#fff"/><path d="M.5.5L6 5l5.5-4.5" fill="none" stroke="#fff"/></svg><span>Email :<br>info@metrivanelabs.com</span></li>
      </ul>
      <h4 class="footer-heading" style="left:489px">SIGN UP TO RECEIVE EMAIL</h4>
      <div class="signup">
        <p>Excepteur sint occaecat cupidatat non proident, sunt in culpa qui Nemo enim ipsam vo-</p>
        <div class="signup__input">Enter Email</div>
        <div class="signup__btn">SUBSCRIBE</div>
      </div>
      <div class="footer-bar">Copyright © Metrivane Labs 2021. All rights reserved. | Privacy Policy</div>
    </footer>
  </section>

  <!-- Single post page -->
  <section class="page page--post">
    <header class="site-header">
      <div class="brand" style="left:64px"><span class="brand__mark"></span>Metrivane Labs</div>
      <nav class="nav" style="left:287px"><span class="nav__item--active">Home</span><span>About us</span><span>Our Service</span><span>Blog</span><span>Contact</span></nav>
      <div class="btn-start" style="left:618px">GET STARTED</div>
    </header>

    <h2 class="section-title" style="top:76px">Our Blog Posts</h2>

    <div class="media" role="img" aria-label="Photo of a businessman behind a transparent analytics dashboard" style="left:94px;top:136px;width:592px;height:287px;background:linear-gradient(135deg,#141b2a,#2a3c5c 50%,#10151f)"></div>
    <div class="date-badge" style="left:106px;top:150px;width:39px;height:39px;font-size:9.5px;line-height:10.5px">OCT<br>2021</div>

    <article class="article">
      <h3 class="article__title">Lorem Ipsum is simply dummy text of the printing and typesetting industry. Lorem printing and typesetting industry. Lorem Ipsum is simply dummy text</h3>
      <div class="meta">
        <span><svg width="9" height="8" viewBox="0 0 9 8"><path d="M1 1h7v4.5H4L2 7V5.5H1z" fill="none" stroke="#5b5fd6"/></svg>2 comments</span>
        <span><svg width="8" height="8" viewBox="0 0 8 8"><circle cx="4" cy="2.2" r="2" fill="#5b5fd6"/><path d="M0 8c0-2.5 2-3.5 4-3.5S8 5.5 8 8z" fill="#5b5fd6"/></svg>by Nora</span>
      </div>
      <p class="article__text">Lorem Ipsum is simply dummy text of the printing and typesetting industry. Lorem Ipsum has been the industry's standard dummy text ever since the 1500s, when an unknown printer took a galley of type and scrambled it to make a type specimen book. It has survived not only five centuries, but also the leap into electronic typesetting, remaining essentially Lorem Ipsum is simply dummy text of the printing and typesetting industry. Lorem Ipsum has been the industry's standard dummy text ever since the 1500s, when an unknown printer took a galley of type and scrambled it to make a type specimen book. It has survived not only five centurie</p>
      <p class="article__text">typesetting, remaining essentially Lorem Ipsum is simply dummy text of the printing and typesetting industry. Lorem Ipsum has been the industry's standard dummy text ever since the 1500s, when an unknown printer took a galley of type and scrambled it to make a type specimen book. It has survived not only five centuries, but also the leap into electronic typesetting, remaining essentially Lorem Ipsum is simply dummy text of the printing and typesetting industry. Lorem Ipsum has been the industry's standard dummy text ever since the 1500s, when an unknown printer took a galley of type and scrambled it to make a type specimen book. It has survived not only five centuries, but also the leap into electronic typesetting, remaining essentially Lorem Ipsum is simply dummy text of the printing and typesetting industry. Lorem Ipsum has been the industry's standard dummy text ever since the 1500s, when an unknown printer took a galley of type and scrambled it to make a type specimen book. It has survived not only five centuries, but also the leap into electronic typesetting, remaining essentially</p>
    </article>

    <footer class="site-footer">
      <div class="brand"><span class="brand__mark"></span>Metrivane Labs</div>
      <p class="footer-about">Sed ut perspiciatis unde omnis iste natus error sit voluptatem accusantium dolorque laudantium, totam rem aperiam, eaque ipsa quae ab illo inventore veritatis et quasi</p>
      <div class="socials"><span></span><span></span><span></span><span></span></div>
      <h4 class="footer-heading" style="left:311px">CONTACT US</h4>
      <ul class="contact-list">
        <li><svg width="10" height="13" viewBox="0 0 10 13"><path d="M5 12S1 7.5 1 4.8a4 4 0 0 1 8 0C9 7.5 5 12 5 12z" fill="none" stroke="#fff"/><circle cx="5" cy="4.8" r="1.4" fill="none" stroke="#fff"/></svg><span>Metrivane Labs<br>250 ipsam voluptatem<br>quia voluptas</span></li>
        <li><svg width="11" height="11" viewBox="0 0 11 11"><path d="M2 1l2 2.5-1.2 1.2a6 6 0 0 0 3.5 3.5L7.5 7 10 9l-1.3 1.5C4.5 10.5.5 6.5.5 2.3z" fill="none" stroke="#fff"/></svg><span>Phone :<br>555-0142-3100</span></li>
        <li><svg width="12" height="9" viewBox="0 0 12 9"><rect x=".5" y=".5" width="11" height="8" fill="none" stroke="#fff"/><path d="M.5.5L6 5l5.5-4.5" fill="none" stroke="#fff"/></svg><span>Email :<br>info@metrivanelabs.com</span></li>
      </ul>
      <h4 class="footer-heading" style="left:489px">SIGN UP TO RECEIVE EMAIL</h4>
      <div class="signup">
        <p>Excepteur sint occaecat cupidatat non proident, sunt in culpa qui Nemo enim ipsam vo-</p>
        <div class="signup__input">Enter Email</div>
        <div class="signup__btn">SUBSCRIBE</div>
      </div>
      <div class="footer-bar">Copyright © Metrivane Labs 2021. All rights reserved. | Privacy Policy</div>
    </footer>
  </section>

</div>
</body>
</html>
```